Business Card Design

Lotside Ledger is an online automotive resource on a national scale specifically targeting lease purchases for new cars. Our Online and app platform allow prospective lease clients to scan a window sticker while at a franchise dealership and instantly receive a lease quote at what we call the sweet spot. Lotside Ledger offers price transparency during the lease process to allow average people the confidence in the lease process and takes away any fear of the big franchise dealers.
Lotside ledger allows ordinary lease customers to know they are getting a low price lease and not overpaying. Never overpay again

Industry/Entity Type

Automotive

Contact Information for Business Card

Lotside Ledger
Marcus Todwell (President of operations)
Phone: 888-302-7716
Cell: 561-448-2053

```html
<!DOCTYPE html>
<html lang="en">
<head>
<meta charset="utf-8">
<title>Lotside Ledger — Business Card</title>
<link href="https://fonts.googleapis.com/css2?family=Lato:wght@400;700;900&display=swap" rel="stylesheet">
<style>
  :root {
    --page-bg: #1c1c1e;
    --blue-light: #4a8fe0;
    --blue-mid: #1f5bb5;
    --blue-deep: #123a86;
    --card-white: #f7f7f7;
    --tile-grey: #e6e6e6;
    --ink: #1a1a1a;
    --ink-soft: #3a3a3a;
    --title-blue: #3a4a7a;
    --white: #ffffff;
  }
  * { box-sizing: border-box; margin: 0; padding: 0; }
  html, body {
    width: 1200px; height: 873px; overflow: hidden;
    background: var(--page-bg);
    font-family: "Lato", Arial, sans-serif;
  }
  .canvas { position: relative; width: 1200px; height: 873px; }

  .card {
    position: absolute;
    width: 530px; height: 310px;
    border-radius: 22px;
    overflow: hidden;
    box-shadow: 0 18px 40px rgba(0,0,0,.55);
  }

  /* Front: blue */
  .card--front {
    left: 45px; top: 190px;
    background: radial-gradient(ellipse at 45% 40%, var(--blue-light) 0%, var(--blue-mid) 45%, var(--blue-deep) 100%);
  }
  .card--front .wordmark {
    position: absolute; left: 130px; top: 88px;
    color: var(--white);
    font-weight: 900; font-size: 40px; line-height: .95;
    letter-spacing: .5px; text-transform: uppercase;
  }
  .card--front .url-band {
    position: absolute; left: 118px; right: 0; top: 190px; height: 30px;
    background: var(--white);
    border-radius: 15px 0 0 15px;
    display: flex; align-items: center; padding-left: 22px;
    color: var(--blue-mid);
    font-weight: 700; font-size: 15px; letter-spacing: 3px;
  }

  /* Back: white */
  .card--back {
    left: 625px; top: 370px;
    background: var(--card-white);
  }
  .card--back .tile-field {
    position: absolute; inset: 0;
    background: linear-gradient(135deg, var(--card-white) 0%, var(--tile-grey) 55%, var(--card-white) 100%);
    opacity: .8;
  }
  .card--back .wordmark {
    position: absolute; left: 130px; top: 40px;
    color: var(--ink);
    font-weight: 900; font-size: 38px; line-height: .95;
    text-transform: uppercase;
  }
  .card--back .rule-top {
    position: absolute; left: 130px; right: 40px; top: 128px;
    height: 2px; background: var(--ink);
  }
  .person { position: absolute; left: 40px; top: 170px; }
  .person__name {
    font-weight: 900; font-size: 22px; color: var(--ink);
  }
  .person__title {
    font-size: 15px; color: var(--title-blue); margin-top: 2px;
  }
  .card--back .rule-name {
    position: absolute; left: 250px; right: 40px; top: 186px;
    height: 2px; background: var(--ink);
  }
  .contacts {
    position: absolute; left: 40px; top: 232px;
    list-style: none; font-size: 14px; color: var(--ink-soft);
  }
  .contacts li { display: flex; align-items: center; gap: 12px; height: 22px; }
  .contacts svg { width: 16px; height: 16px; fill: var(--ink-soft); flex: none; }
</style>
</head>
<body>
<main class="canvas">

  <section class="card card--front" aria-label="Card front">
    <div class="wordmark">Lotside<br>Ledger</div>
    <div class="url-band">www.LotsideLedger.com</div>
  </section>

  <section class="card card--back" aria-label="Card back">
    <div class="tile-field" role="img" aria-label="Soft grey checkered tile background pattern"></div>
    <div class="wordmark">Lotside<br>Ledger</div>
    <div class="rule-top"></div>

    <div class="person">
      <p class="person__name">Marcus Todwell</p>
      <p class="person__title">Director of Operations</p>
    </div>
    <div class="rule-name"></div>

    <ul class="contacts">
      <li>
        <svg viewBox="0 0 16 16" aria-hidden="true"><path d="M1 5c0-2 3-3 7-3s7 1 7 3v1h-4V5H5v1H1z M3 7h10l1 7H2z"/></svg>
        888 302 7716
      </li>
      <li>
        <svg viewBox="0 0 16 16" aria-hidden="true"><path d="M4 0h8a1 1 0 0 1 1 1v14a1 1 0 0 1-1 1H4a1 1 0 0 1-1-1V1a1 1 0 0 1 1-1zm.5 2v11h7V2z"/></svg>
        561-448-2053
      </li>
      <li>
        <svg viewBox="0 0 16 16" aria-hidden="true"><path d="M1 3h14v10H1z M2 4l6 5 6-5" fill="none" stroke="#3a3a3a" stroke-width="1.5"/></svg>
        MarcusT@LotsideLedger.com
      </li>
    </ul>
  </section>

</main>
</body>
</html>
```